New Business Card Design

We need a business card design for a new company based in Sydney called "Hearth and Ember". This is an online buisness which will have an online store providing imported homewares.
We are looking for something that is different, perhaps even in shape and using the logo that was designed by Pixel Meadow.

Attached document is a basic example I want to see more creative versions.

Target Market(s)

Homewares, Interior Design

Industry/Entity Type

Business

Contact Information for Business Card

Company Logo
Company Name
Industry area
Name
Position
Phone
Email
Website
Motto

Requirements
Must have
• Logo
Nice to have
• Social website logos - Friendlane, Glimmerly, Quipster, Boardwhim, Zumvo+

```html
<!DOCTYPE html>
<html lang="en">
<head>
<meta charset="utf-8">
<title>Hearth and Ember – Business Card</title>
<link rel="stylesheet" href="https://fonts.googleapis.com/css2?family=Lato:wght@400;700&display=swap">
<style>
  :root {
    --backdrop: #d8cec3;
    --frost-light: #f2f1ef;
    --frost-mid: #d9d8d6;
    --frost-dark: #bdbcba;
    --ink-dark: #1c1b1b;
    --ink-mid: #2e2c2b;
    --gold: #b3844f;
    --gold-light: #d9ae74;
    --gold-deep: #7a5227;
    --text-light: #e6e3df;
    --text-rose: #c9a8a0;
    --logo-ink: #2a2624;
  }
  html, body {
    margin: 0;
    padding: 0;
    width: 1200px;
    height: 970px;
    overflow: hidden;
    background: var(--backdrop);
    font-family: "Lato", sans-serif;
  }
  .card {
    position: absolute;
    left: 172px;
    top: 247px;
    width: 856px;
    height: 476px;
    border-radius: 14px;
    overflow: hidden;
    box-shadow: 0 10px 30px rgba(60, 45, 30, 0.25);
  }
  .card-art {
    position: absolute;
    inset: 0;
    width: 856px;
    height: 476px;
  }
  .brand-name {
    position: absolute;
    left: 520px;
    top: 124px;
    width: 290px;
    text-align: center;
    font-size: 31px;
    font-weight: 700;
    color: var(--logo-ink);
    letter-spacing: 0.5px;
  }
  .holder {
    position: absolute;
    left: 82px;
    top: 208px;
    color: var(--text-light);
  }
  .holder-name {
    font-size: 27px;
    font-weight: 700;
    color: var(--gold);
    line-height: 1.2;
  }
  .holder-role {
    font-size: 22px;
    line-height: 1.3;
  }
  .address {
    position: absolute;
    left: 84px;
    top: 300px;
    font-size: 20px;
    line-height: 28px;
    color: var(--text-light);
  }
  .contact-list {
    position: absolute;
    left: 46px;
    top: 370px;
    margin: 0;
    padding: 0;
    list-style: none;
  }
  .contact-item {
    display: flex;
    align-items: center;
    height: 29px;
    font-size: 20px;
    color: var(--text-rose);
  }
  .contact-item svg {
    width: 20px;
    height: 20px;
    margin-right: 18px;
    flex: none;
  }
  .contact-phone { letter-spacing: 3.5px; }
  .social-list {
    position: absolute;
    right: 28px;
    bottom: 22px;
    display: flex;
    gap: 10px;
    margin: 0;
    padding: 0;
    list-style: none;
  }
  .social-item {
    display: flex;
    align-items: center;
    gap: 4px;
    font-size: 11px;
    font-weight: 700;
    color: var(--gold);
  }
  .social-dot {
    width: 9px;
    height: 9px;
    border-radius: 50%;
    background: var(--gold);
  }
</style>
</head>
<body>
  <div class="card">
    <svg class="card-art" viewBox="0 0 856 476" xmlns="http://www.w3.org/2000/svg">
      <defs>
        <linearGradient id="frost" x1="0" y1="0" x2="1" y2="1">
          <stop offset="0" stop-color="var(--frost-light)"/>
          <stop offset="0.5" stop-color="var(--frost-mid)"/>
          <stop offset="1" stop-color="var(--frost-dark)"/>
        </linearGradient>
        <linearGradient id="darkPanel" x1="0" y1="0" x2="0" y2="1">
          <stop offset="0" stop-color="var(--ink-mid)"/>
          <stop offset="1" stop-color="var(--ink-dark)"/>
        </linearGradient>
        <linearGradient id="goldBand" x1="0" y1="0" x2="1" y2="0">
          <stop offset="0" stop-color="var(--gold-deep)"/>
          <stop offset="0.5" stop-color="var(--gold-light)"/>
          <stop offset="1" stop-color="var(--gold)"/>
        </linearGradient>
      </defs>
      <rect class="card-surface" width="856" height="476" fill="url(#frost)"/>
      <path class="wave-panel" d="M0,108 L40,108 C200,110 330,170 430,250 C520,320 600,365 700,365 C780,365 830,330 856,300 L856,476 L0,476 Z" fill="url(#darkPanel)"/>
      <path class="gold-band" d="M470,283 C560,345 630,372 710,372 C780,372 830,345 856,322 L856,358 C830,380 780,402 700,400 C610,398 540,345 470,283 Z" fill="url(#goldBand)"/>
      <path class="gold-rule" d="M40,106 C200,108 330,168 430,248 C520,318 600,363 700,363 C780,363 830,328 856,298" fill="none" stroke="var(--gold)" stroke-width="2.5"/>
      <rect class="side-strip" x="34" y="108" width="14" height="368" fill="var(--frost-mid)" opacity="0.85"/>
      <rect class="sprig-ornament" x="34" y="44" width="60" height="62" rx="8" fill="var(--gold)" opacity="0.55" role="img" aria-label="Small gold leaf sprig ornament"/>
    </svg>

    <div class="brand-name">Hearth and Ember</div>

    <div class="holder">
      <div class="holder-name">Marcus Elway</div>
      <div class="holder-role">Director</div>
    </div>

    <div class="address">
      Unit 4, Ember Lane<br>
      Hearthvale 4321 Queensland AU
    </div>

    <ul class="contact-list">
      <li class="contact-item contact-phone">
        <svg viewBox="0 0 20 20" aria-hidden="true"><path d="M3 6 Q10 1 17 6 L15 9 L13 7 L7 7 L5 9 Z M5 10 H15 L16 17 H4 Z" fill="var(--gold)"/></svg>
        0798765432
      </li>
      <li class="contact-item">
        <svg viewBox="0 0 20 20" aria-hidden="true"><rect x="2" y="5" width="16" height="11" fill="none" stroke="var(--gold)" stroke-width="1.8"/><path d="M2 5 L10 11 L18 5" fill="none" stroke="var(--gold)" stroke-width="1.8"/></svg>
        me@hearthandember.com.au
      </li>
      <li class="contact-item">
        <svg viewBox="0 0 20 20" aria-hidden="true"><circle cx="10" cy="10" r="8" fill="none" stroke="var(--gold)" stroke-width="1.6"/><ellipse cx="10" cy="10" rx="3.5" ry="8" fill="none" stroke="var(--gold)" stroke-width="1.4"/><path d="M2 10 H18 M4 6 H16 M4 14 H16" stroke="var(--gold)" stroke-width="1.2"/></svg>
        www.hearthandember.com.au
      </li>
    </ul>

    <ul class="social-list">
      <li class="social-item"><span class="social-dot"></span>Friendlane</li>
      <li class="social-item"><span class="social-dot"></span>Quipster</li>
      <li class="social-item"><span class="social-dot"></span>Glimmerly</li>
      <li class="social-item"><span class="social-dot"></span>Boardwhim</li>
      <li class="social-item"><span class="social-dot"></span>Zumvo+</li>
    </ul>
  </div>
</body>
</html>
```